Business Cards and Stationery - Real Estate
See "information" and "additional comments"
Business Cards and Stationery - Real Estate - Real Estate
Creative Brief
Professional
Anselm Varga
Managing Broker
4382 SW Route 14, Ste 305 Vancouver, WA 98671
Direct - 360-555-0147
Cell - 360-555-0193
anselm@fernloftpm.example
www.fernlofthomes.example
Licensed in OR & WA
We want to use UV spotting on our cards. Here is a video link from the printing company we are using. If you are unfamiliar with creating files for UV spotting, it requires one file for the card and a second mask file for the UV spotting. https://www.clipvault.example/watch?v=Qx7rLm2PzA1 I've uploaded the template files to use from Zentra Print along with our Adobe Illustrator Logo files and a head shot. We probably don't want a head shot on the card, but have uploaded just in case. Please use Adobe Illustrator.
Probably just the logo. Something that is clean, possible a repeated design such as the logo. Would like to consider UV spotting on back. Try searching for "business cards spot uv" on Google, then look at the "images" link.
SiteAdmin SiteAdmin
Dear Designers, Kindly follow the below mention instructions by the Project holder for better and improve designs: We want to use spot UV on our cards, front and back. Here is a video Link from the printing company we are using. If you are unfamiliar with creating file for Spot UV, it requires one file for the card and a second mask file for the UV spotting. https://www.clipvault.example/watch?v=Qx7rLm2PzA1 Use your creativity, but a couple ideas for the back would be to repeat our logo over and over across the entire back. It may be nice to somehow put our website within those repeated logos. Or it may not be nice, depending on how it looks. You could also just make our logo with URL on the back. For the front, you will have to be creative to make it work. Our logo could be UV spotted. And then probably some sort of nice design that covers a portion of the front, keeping in mind that the uv spot coating design can overlap anything. Or maybe it would look best to only spot uv our logo. The content for the card is in our creative brief. We would also like to include "We Love Referrals!" somewhere on the card. Here are a few images for some ideas. Keep in mind that we don't want a copy of what is done with these ideas. They are simply ideas of what can be done with UV spotting. https://pressglow.example/assets/images/gallery/business-cards/images/a1b2c3d4e5f60718293a4b5c6d7e8f90.png https://pressglow.example/assets/uploads/spot_uv_marlow_business_cards.jpg http://media.shopweave.example/51730264/Renata-Pell-spot-gloss-silver-foil-spot-uv-silk-unique-cool-business-cards_full.jpeg http://www.quartzlinecards.example/images/img-gallery/silk-business-card-with-spot-uv-harrow-cellars.jpg http://i01.i.tradepix.example/wsphoto/v2/813406572_2/Custom-Spot-UV-business-card-matt-coated-paper-350gsm-High-quality.jpg http://www.newswire.example/64028195-silk-laminated-business-cards-with-spot-uv.jpg http://www.atelier-cartes-nord.example/wp-content/uploads/2010/10/carte-commerciale-vernis-selectif.jpg https://pressglow.example/assets/uploads/spot_uv_cards_dravetek.jpg http://www.calloutmailers.example/wp/wp-content/uploads/2013/03/zebra-orange-spot-uv-business-card1.png http://layoutharbor.example/wp-content/uploads/2013/04/square-business-card-29.jpg
fernloft47 fernloft47
I forgot to add on that last comment, that the black designs are way to dark for our tastes. Blue on the back looks nice. We prefer the lighter designs on the front of the card.
We are looking for double sided cards with rounded corners and some UV spotting on both sides. We like the design of #96 on the back side, however it looks like there may be some silver foil on the logo. We won't be doing foil, just spotting. There are a lot of nice designs so far, but we need to have the combination of rounded corners and UV spotting. Thanks.

```html
<!DOCTYPE html>
<html lang="en">
<head>
<meta charset="utf-8">
<title>Fernloft Properties – Business Cards</title>
<link rel="stylesheet" href="https://fonts.googleapis.com/css2?family=Montserrat:wght@700&family=Open+Sans:ital,wght@0,400;0,600;1,400&display=swap">
<style>
  :root {
    --backdrop: #e9e6e1;
    --card-white: #ffffff;
    --brand-blue: #1f4e96;
    --brand-blue-deep: #163d7a;
    --swoosh-grey: #8a8d93;
    --swoosh-light: #c9cbcf;
    --ink: #3b3f46;
    --on-blue: #ffffff;
  }
  * { box-sizing: border-box; margin: 0; padding: 0; }
  html, body {
    width: 1200px;
    height: 828px;
    overflow: hidden;
    background: var(--backdrop);
  }
  .sheet {
    position: relative;
    width: 1200px;
    height: 828px;
  }
  .card {
    position: absolute;
    width: 540px;
    height: 309px;
    background: var(--card-white);
    border-radius: 8px;
    overflow: hidden;
    box-shadow: 0 6px 18px rgba(0, 0, 0, 0.14);
  }
  .card--back  { left: 40px;  top: 200px; }
  .card--front { left: 620px; top: 320px; }
  .card__swoosh {
    position: absolute;
    inset: 0;
    width: 100%;
    height: 100%;
  }

  /* back side */
  .back-mark {
    position: absolute;
    left: 70px;
    top: 118px;
    display: flex;
    align-items: center;
    gap: 12px;
  }
  .back-mark__square {
    width: 34px;
    height: 34px;
    border: 4px solid var(--brand-blue);
    border-radius: 4px;
  }
  .back-mark__name {
    font-family: "Montserrat", sans-serif;
    font-weight: 700;
    font-size: 36px;
    letter-spacing: 1px;
    color: var(--brand-blue);
  }

  /* front side */
  .front-identity {
    position: absolute;
    left: 36px;
    top: 82px;
  }
  .front-identity__mark {
    display: flex;
    align-items: center;
    gap: 10px;
  }
  .front-identity__square {
    width: 26px;
    height: 26px;
    border: 3px solid var(--brand-blue);
    border-radius: 3px;
  }
  .front-identity__name {
    font-family: "Montserrat", sans-serif;
    font-weight: 700;
    font-size: 26px;
    letter-spacing: 1px;
    color: var(--brand-blue);
    line-height: 1;
  }
  .front-identity__sub {
    font-family: "Montserrat", sans-serif;
    font-weight: 700;
    font-size: 10px;
    letter-spacing: 6px;
    color: var(--brand-blue);
    margin: 6px 0 0 36px;
  }
  .person {
    margin-top: 28px;
  }
  .person__name {
    font-family: "Open Sans", sans-serif;
    font-weight: 600;
    font-size: 17px;
    letter-spacing: 1px;
    color: var(--brand-blue);
  }
  .person__role,
  .person__license {
    font-family: "Open Sans", sans-serif;
    font-weight: 400;
    font-size: 11px;
    color: var(--ink);
    margin-top: 2px;
  }
  .referral-note {
    position: absolute;
    left: 36px;
    bottom: 26px;
    font-family: "Open Sans", sans-serif;
    font-style: italic;
    font-weight: 400;
    font-size: 11px;
    color: var(--brand-blue);
  }
  .contact-list {
    position: absolute;
    left: 338px;
    top: 78px;
    width: 192px;
    list-style: none;
    font-family: "Open Sans", sans-serif;
    font-size: 9.5px;
    line-height: 1.35;
    color: var(--on-blue);
  }
  .contact-list__item {
    display: flex;
    align-items: flex-start;
    gap: 7px;
    margin-bottom: 9px;
  }
  .contact-list__icon {
    width: 11px;
    height: 11px;
    flex: none;
    margin-top: 1px;
  }
</style>
</head>
<body>
<main class="sheet">

  <section class="card card--back" aria-label="Business card, back side">
    <svg class="card__swoosh" viewBox="0 0 540 309" aria-hidden="true">
      <path d="M330,0 C400,70 360,220 250,309 L540,309 L540,0 Z" fill="var(--swoosh-light)"/>
      <path d="M352,0 C418,74 378,224 272,309 L540,309 L540,0 Z" fill="var(--card-white)"/>
      <path d="M366,0 C432,80 390,226 286,309 L540,309 L540,0 Z" fill="var(--swoosh-grey)"/>
      <path d="M388,0 C452,86 412,230 312,309 L540,309 L540,0 Z" fill="var(--brand-blue)"/>
      <path d="M470,0 C510,60 500,180 430,309 L540,309 L540,0 Z" fill="var(--brand-blue-deep)" opacity="0.35"/>
    </svg>
    <div class="back-mark">
      <span class="back-mark__square"></span>
      <span class="back-mark__name">Fernloft</span>
    </div>
  </section>

  <section class="card card--front" aria-label="Business card, front side">
    <svg class="card__swoosh" viewBox="0 0 540 309" aria-hidden="true">
      <path d="M250,0 C330,70 300,220 210,309 L540,309 L540,0 Z" fill="var(--swoosh-light)"/>
      <path d="M272,0 C350,76 318,224 232,309 L540,309 L540,0 Z" fill="var(--card-white)"/>
      <path d="M286,0 C364,82 330,226 246,309 L540,309 L540,0 Z" fill="var(--swoosh-grey)"/>
      <path d="M306,0 C384,88 350,230 270,309 L540,309 L540,0 Z" fill="var(--brand-blue)"/>
    </svg>

    <div class="front-identity">
      <div class="front-identity__mark">
        <span class="front-identity__square"></span>
        <span class="front-identity__name">FERNLOFT</span>
      </div>
      <div class="front-identity__sub">PROPERTIES</div>
      <div class="person">
        <div class="person__name">ANSELM VARGA</div>
        <div class="person__role">Managing Broker</div>
        <div class="person__license">Licensed in OR &amp; WA</div>
      </div>
    </div>

    <p class="referral-note">We Love Referrals!</p>

    <ul class="contact-list">
      <li class="contact-list__item">
        <svg class="contact-list__icon" viewBox="0 0 12 12" aria-hidden="true"><circle cx="6" cy="6" r="6" fill="var(--on-blue)"/><path d="M4,3 L5.2,3 L5.6,4.6 L4.9,5.2 Q5.6,6.6 6.8,7.1 L7.4,6.4 L9,6.8 L9,8 Q6,8.6 4,4.2 Z" fill="var(--brand-blue)"/></svg>
        <span>Direct - 360-555-0147</span>
      </li>
      <li class="contact-list__item">
        <svg class="contact-list__icon" viewBox="0 0 12 12" aria-hidden="true"><circle cx="6" cy="6" r="6" fill="var(--on-blue)"/><rect x="4.2" y="2.6" width="3.6" height="6.8" rx="0.6" fill="var(--brand-blue)"/></svg>
        <span>Cell - 360-555-0193</span>
      </li>
      <li class="contact-list__item">
        <svg class="contact-list__icon" viewBox="0 0 12 12" aria-hidden="true"><circle cx="6" cy="6" r="6" fill="var(--on-blue)"/><rect x="3" y="4" width="6" height="4.2" fill="var(--brand-blue)"/><path d="M3,4 L6,6.4 L9,4" stroke="var(--on-blue)" stroke-width="0.7" fill="none"/></svg>
        <span>anselm@fernloftpm.example</span>
      </li>
      <li class="contact-list__item">
        <svg class="contact-list__icon" viewBox="0 0 12 12" aria-hidden="true"><circle cx="6" cy="6" r="6" fill="var(--on-blue)"/><circle cx="6" cy="6" r="3" fill="none" stroke="var(--brand-blue)" stroke-width="0.9"/><path d="M3,6 H9 M6,3 V9" stroke="var(--brand-blue)" stroke-width="0.7"/></svg>
        <span>www.fernlofthomes.example</span>
      </li>
      <li class="contact-list__item">
        <svg class="contact-list__icon" viewBox="0 0 12 12" aria-hidden="true"><circle cx="6" cy="6" r="6" fill="var(--on-blue)"/><path d="M6,9.6 L3.9,6 A2.4,2.4 0 1 1 8.1,6 Z" fill="var(--brand-blue)"/><circle cx="6" cy="4.9" r="0.9" fill="var(--on-blue)"/></svg>
        <span>4382 SW Route 14, Ste 305<br>Vancouver, WA 98671</span>
      </li>
    </ul>
  </section>

</main>
</body>
</html>
```